Buisness card

**Front Side:**

**[Your Company Logo]**
**Steadfast Upkeep Engineering**
*Keeping Your Equipment Running Smoothly*

**Contact Information:**
- **Name:** [dale Harwick
- **Title:** [owner
- **Phone:** [5073918246
- **Email:** dale@suevx.com

**Back Side:**

**Services Offered:**
- Routine Inspections
- Equipment Maintenance
- Emergency Repairs
- Consultation Services
- New installs
Tag line
Be proactive not reactive

```html
<!DOCTYPE html>
<html lang="en">
<head>
<meta charset="utf-8">
<title>Steadfast Upkeep Engineering – Business Card</title>
<link href="https://fonts.googleapis.com/css2?family=Montserrat:wght@500;600;700&display=swap" rel="stylesheet">
<style>
  :root {
    --backdrop: #d6d7db;
    --card: #ffffff;
    --navy: #25306b;
    --cyan: #2bc3ef;
    --ink: #2f2f33;
    --black: #111111;
  }
  * { margin: 0; padding: 0; box-sizing: border-box; }
  html, body { width: 1200px; height: 1129px; overflow: hidden; }
  body { background: var(--backdrop); font-family: 'Montserrat', sans-serif; position: relative; }

  .card {
    position: absolute;
    width: 790px;
    height: 452px;
    background: var(--card);
    border-radius: 36px;
  }
  .card--front { left: 204px; top: 92px; }
  .card--back  { left: 205px; top: 584px; }

  .brand-mark {
    position: absolute;
    border-radius: 50%;
    background: var(--navy);
  }
  .card--front .brand-mark { left: 101px; top: 170px; width: 126px; height: 126px; }
  .card--back .brand-mark  { left: 48px; top: 41px; width: 90px; height: 90px; }

  .brand-name {
    position: absolute;
    color: var(--navy);
    font-weight: 700;
    white-space: nowrap;
  }
  .card--front .brand-name { left: 266px; top: 188px; font-size: 31px; line-height: 40px; }
  .card--back .brand-name  { left: 165px; top: 60px; font-size: 21px; line-height: 28px; }

  .tagline {
    position: absolute;
    color: var(--black);
    font-weight: 700;
    white-space: nowrap;
  }
  .card--front .tagline { left: 266px; top: 250px; font-size: 24px; letter-spacing: 0.5px; }
  .card--back .tagline  { left: 168px; top: 100px; font-size: 11.5px; letter-spacing: 0.3px; font-variant: small-caps; }

  .person { position: absolute; left: 29px; top: 222px; }
  .person__name { color: var(--cyan); font-weight: 600; font-size: 36px; line-height: 44px; }
  .person__title { color: var(--ink); font-weight: 500; font-size: 20px; margin-top: 8px; }

  .contact { position: absolute; left: 29px; list-style: none; }
  .contact li { display: flex; align-items: center; gap: 9px; color: var(--ink); font-size: 21px; font-weight: 500; height: 38px; }
  .contact svg { width: 19px; height: 19px; fill: var(--cyan); }
  .contact { top: 352px; }

  .services { position: absolute; right: 33px; top: 170px; text-align: right; }
  .services__heading { color: var(--cyan); font-weight: 700; font-size: 30px; line-height: 36px; margin-bottom: 14px; }
  .services__list { list-style: none; }
  .services__list li { color: var(--ink); font-size: 19px; font-weight: 500; height: 41px; display: flex; justify-content: flex-end; align-items: center; gap: 5px; }
  .services__list li::after { content: ""; width: 7px; height: 7px; border-radius: 50%; background: var(--navy); }
</style>
</head>
<body>
  <section class="card card--front">
    <div class="brand-mark"></div>
    <div class="brand-name">Steadfast Upkeep Engineering</div>
    <div class="tagline">BE PROACTIVE NOT REACTIVE</div>
  </section>

  <section class="card card--back">
    <div class="brand-mark"></div>
    <div class="brand-name">Steadfast Upkeep Engineering</div>
    <div class="tagline">Keeping Your Equipment Running Smoothly</div>

    <div class="person">
      <h1 class="person__name">Dale Harwick</h1>
      <p class="person__title">Owner</p>
    </div>

    <ul class="contact">
      <li>
        <svg viewBox="0 0 24 24" aria-hidden="true"><path d="M3 9c0-3 4-5 9-5s9 2 9 5v2h-5V9H8v2H3z M6 12h12l2 8H4z"/></svg>
        5073918246
      </li>
      <li>
        <svg viewBox="0 0 24 24" aria-hidden="true"><path d="M2 5h20v14H2z M3 6l9 7 9-7" stroke="#fff" stroke-width="1.5"/></svg>
        dale@suevx.com
      </li>
    </ul>

    <div class="services">
      <h2 class="services__heading">OUR SERVICES</h2>
      <ul class="services__list">
        <li>Routine Inspections</li>
        <li>Equipment Maintenance</li>
        <li>Emergency Repairs</li>
        <li>Consultation Services</li>
        <li>New installs</li>
      </ul>
    </div>
  </section>
</body>
</html>
```